Design for product lable
MERO LUX
COMMING SOON
background design for nutrition products
such as whey protein powders Cretin and so on
this well be our background style
all the fallowing products gonna look nearly the same so the wining design well work on all other products we produce background our bottle color is black we have blue and gold on our logo
athlete, mostly fitness and bodybuilders
and all others sports
it must come in 4 flavor variants : chocolate, vanilla, strawberry,banana
pleas avoid using to many braid colors
try to give a royal look to it thank you
remember it is 250 because separately for each product if you are a wining project then we make a deal what we gonna pay for the each fallowing product
amino profile total hight 6cm
weight 12 cm
color wight or must much whit the label color or whit background blact text
this is a bad resolution so pleas make new charts

```html
<!DOCTYPE html>
<html lang="en">
<head>
<meta charset="utf-8">
<title>MERO LUX – Vanilla Label</title>
<link href="https://fonts.googleapis.com/css2?family=Cinzel:wght@400;700&family=Roboto+Condensed:wght@400;700&display=swap" rel="stylesheet">
<style>
  :root{
    --stage:#050505;
    --navy-deep:#14165a;
    --navy:#232a8c;
    --navy-light:#3a3fb0;
    --gold:#d9a546;
    --gold-light:#f3d38a;
    --brand-orange:#e8a12a;
    --white:#ffffff;
    --ink:#dfe3ff;
    --panel-line:rgba(217,165,70,.55);
  }
  *{box-sizing:border-box;margin:0;padding:0}
  html,body{width:1200px;height:799px;overflow:hidden;background:var(--stage)}
  .label{
    position:absolute;left:40px;top:140px;width:1120px;height:520px;
    background:radial-gradient(ellipse at 50% 40%,var(--navy-light) 0%,var(--navy) 45%,var(--navy-deep) 100%);
    border-top:6px solid var(--gold);border-bottom:6px solid var(--gold);
    display:grid;grid-template-columns:360px 400px 360px;
    font-family:"Roboto Condensed",Arial,sans-serif;color:var(--ink);
  }
  .panel{padding:34px 28px;position:relative}
  .panel--side{font-size:11px;line-height:1.45}
  .panel--left{border-right:1px solid var(--panel-line)}
  .panel--right{border-left:1px solid var(--panel-line)}
  .intro{margin-bottom:22px}
  .table-title{font-weight:700;font-size:14px;color:var(--white);margin:0 0 6px}
  .data-table{width:100%;border-collapse:collapse;margin-bottom:22px;border:1px solid var(--ink)}
  .data-table td{padding:3px 8px;border-bottom:1px solid rgba(223,227,255,.4)}
  .data-table td:last-child{text-align:right}
  .facts{border:2px solid var(--white);padding:6px 8px;margin-bottom:18px;color:var(--white)}
  .facts__title{font-weight:700;font-size:20px;border-bottom:4px solid var(--white);margin-bottom:4px}
  .facts__row{display:flex;justify-content:space-between;border-bottom:1px solid rgba(255,255,255,.5);padding:2px 0}
  .product-side{font-family:"Cinzel",Georgia,serif;font-size:24px;font-weight:700;color:var(--white);margin-bottom:8px}
  .side-copy{margin-bottom:10px}
  .panel--front{display:flex;align-items:center;justify-content:center}
  .front-frame{position:absolute;inset:18px 14px;width:calc(100% - 28px);height:calc(100% - 36px)}
  .front-content{position:relative;text-align:center;display:flex;flex-direction:column;align-items:center}
  .brand{display:flex;align-items:center;gap:8px;font-weight:700;font-size:18px;letter-spacing:1px;color:var(--brand-orange);margin-bottom:26px}
  .brand__dot{width:14px;height:14px;border-radius:50%;background:var(--brand-orange)}
  .product-name{font-family:"Cinzel",Georgia,serif;font-weight:700;font-size:54px;color:var(--white);letter-spacing:1px;line-height:1;padding-bottom:10px;border-bottom:2px solid var(--gold)}
  .protein-types{font-family:"Cinzel",Georgia,serif;font-size:11px;color:var(--gold-light);letter-spacing:1px;margin-top:8px}
  .flavor{font-family:"Cinzel",Georgia,serif;font-size:30px;color:var(--white);letter-spacing:1px;margin-top:56px;padding-top:14px;width:250px;border-top:1.5px solid var(--gold)}
</style>
</head>
<body>
<main class="label">
  <section class="panel panel--side panel--left">
    <p class="intro">Premium blend crafted for lean muscle support and steady recovery after hard training.</p>
    <h3 class="table-title">Per Serving (30 g)</h3>
    <table class="data-table">
      <tr><td>Protein</td><td>24 g</td></tr>
      <tr><td>Carbs</td><td>3 g</td></tr>
      <tr><td>Fat</td><td>1 g</td></tr>
      <tr><td>Calories</td><td>120</td></tr>
    </table>
    <h3 class="table-title">Amino Acid Profile</h3>
    <table class="data-table">
      <tr><td>Leucine</td><td>2.6 g</td></tr>
      <tr><td>Isoleucine</td><td>1.5 g</td></tr>
      <tr><td>Valine</td><td>1.4 g</td></tr>
      <tr><td>Lysine</td><td>2.2 g</td></tr>
      <tr><td>Glutamine</td><td>4.1 g</td></tr>
    </table>
  </section>

  <section class="panel panel--front">
    <svg class="front-frame" viewBox="0 0 372 472" preserveAspectRatio="none" aria-hidden="true">
      <polygon points="40,2 332,2 370,40 370,432 332,470 40,470 2,432 2,40" fill="none" stroke="#d9a546" stroke-width="2"/>
      <polygon points="52,14 320,14 358,52 358,420 320,458 52,458 14,420 14,52" fill="none" stroke="#f3d38a" stroke-width="1"/>
    </svg>
    <div class="front-content">
      <div class="brand"><span class="brand__dot"></span>VALORIA NUTRITION</div>
      <h1 class="product-name">MERO LUX</h1>
      <p class="protein-types">WHEY ISOLATE · CASEIN · EGG PROTEIN</p>
      <p class="flavor">VANILLA</p>
    </div>
  </section>

  <section class="panel panel--side panel--right">
    <div class="facts">
      <div class="facts__title">Nutrition Facts</div>
      <div class="facts__row"><span>Serving Size</span><span>30 g</span></div>
      <div class="facts__row"><span>Calories</span><span>120</span></div>
      <div class="facts__row"><span>Total Fat</span><span>1 g</span></div>
      <div class="facts__row"><span>Sodium</span><span>60 mg</span></div>
      <div class="facts__row"><span>Total Carbs</span><span>3 g</span></div>
      <div class="facts__row"><span>Protein</span><span>24 g</span></div>
    </div>
    <h2 class="product-side">MERO LUX</h2>
    <p class="side-copy">A triple protein blend of fast whey isolate, slow casein and egg protein for all day muscle support.</p>
    <p class="side-copy">Mix one scoop with 250 ml of cold water or milk after training.</p>
  </section>
</main>
</body>
</html>
```